Nourish Kin Network Australia needs a flyer to update to new style guide and modernise

Nourish Kin Network Australia (NKNA) is looking to update their flyers. NKNA is a volunteer, parent-led, not for profit organisation that supports and advocates for parents and carers of someone with an eating disorder. Attached is some flyers and brochures that we are currently working with, since producing those we have introduced a style guide, also attached. The flyer needs to be visually appealing and professional.We are hoping to combine the NKNA flyer and NKNA Brochure into a single item. We also need to add in our new Uplift support groups.This would replace the back page of the brochure ("NKNA Will endeavour to facilitate and advocate...) Please refer to last pages of style guide for Uplift details.If the document could be produced to allow changes to wording as certain details will need to be refined or edited in the future.

Target Market(s)

Parents and Carers of someone with a life threatening mental illness

Font styles to use
Other font styles liked:
• Avenir Next

Colors

Designer to choose colors to be used in the design.

Requirements
Must have
• NKNA logos and font matching style guide
Nice to have
• Clean and professional looking design, visually appealing
• Easy to read
Should not have
• Upsetting images

```html
<!DOCTYPE html>
<html lang="en">
<head>
<meta charset="utf-8">
<title>Nourish Kin Network Australia – Flyer</title>
<link rel="stylesheet" href="https://fonts.googleapis.com/css2?family=Nunito+Sans:ital,wght@0,400;0,600;0,700;0,800;1,600;1,700;1,800&display=swap">
<style>
  :root{
    --stage:#46524f;
    --purple:#7a1f7e;
    --green:#5aa625;
    --teal:#1aa0c8;
    --red:#c8102e;
    --blue:#2f62a8;
    --ink:#1c1c1c;
    --yellow:#f5e11a;
    --wood-dark:#5a3b22;
    --wood-light:#8a6040;
    --grass-dark:#2f5f12;
    --grass-light:#7cb342;
    --bar:#1396c4;
  }
  *{box-sizing:border-box;margin:0;padding:0}
  html,body{width:1178px;height:1200px;overflow:hidden;background:var(--stage)}
  body{font-family:"Nunito Sans",sans-serif;color:var(--ink)}
  .flyer{position:absolute;left:165px;top:0;width:848px;height:1200px;overflow:hidden;
    background:linear-gradient(180deg,#ffffff 0%,#eef5fb 40%,#dfeef8 62%,#e6f1f0 75%,#ffffff 80%)}
  .photo-hero{position:absolute;right:0;top:0;width:520px;height:400px;
    background:linear-gradient(135deg,#f3f1ec 0%,#e4d2bf 45%,#d9c3ad 60%,#e9ece4 100%)}
  .brand{position:absolute;left:44px;top:48px;display:flex;align-items:center;gap:12px}
  .brand-dot{width:46px;height:46px;border-radius:50%;background:var(--purple)}
  .brand-name{font-weight:700;font-size:17px;color:var(--purple);line-height:1.2;width:190px}
  .wave{position:absolute;left:0;top:260px;width:848px;height:220px}
  .intro{position:absolute;left:0;top:470px;width:848px;text-align:center}
  .headline{color:var(--red);font-weight:700;font-size:42px;line-height:1.02;letter-spacing:.5px}
  .subhead{color:var(--blue);font-weight:600;font-size:25px;line-height:1.15;margin-top:10px}
  .lead{font-size:18px;line-height:1.2;margin-top:8px}
  .promise{color:var(--purple);font-weight:800;font-size:16px;line-height:1.2;margin-top:14px;font-style:italic;text-transform:uppercase}
  .grass{position:absolute;left:0;top:930px;width:848px;height:270px;
    background:linear-gradient(180deg,rgba(124,179,66,0) 0%,var(--grass-light) 22%,var(--grass-dark) 100%)}
  .board{position:absolute;left:150px;top:770px;width:580px;height:230px;border:3px solid var(--yellow);border-radius:10px;
    background:repeating-linear-gradient(180deg,var(--wood-light) 0 30px,var(--wood-dark) 30px 33px),var(--wood-light);
    padding:12px 80px 0 50px;color:#fff}
  .board-title{color:var(--yellow);font-weight:800;font-style:italic;font-size:25px;text-align:center;margin-bottom:8px}
  .reasons{list-style:none;font-size:13px;font-style:italic;font-weight:600;line-height:1.25}
  .reasons li{display:flex;gap:8px;align-items:flex-start;margin-bottom:6px}
  .tick{flex:none;width:14px;height:14px;margin-top:1px}
  .kid-left{position:absolute;left:36px;top:770px;width:120px;height:160px;border-radius:14px;
    background:linear-gradient(180deg,#f3d6c0 0%,#e8955a 45%,#d96f2c 100%)}
  .kid-right{position:absolute;left:738px;top:860px;width:96px;height:170px;border-radius:14px;
    background:linear-gradient(180deg,#f3d6c0 0%,#e2574f 45%,#c8202a 100%)}
  .partner{position:absolute;left:180px;top:1010px;font-size:22px;font-weight:600;color:var(--ink)}
  .pledge{position:absolute;left:400px;top:1020px;width:240px;color:var(--purple);font-weight:700;font-style:italic;font-size:15px;line-height:1.15}
  .contact{position:absolute;display:flex;align-items:center;gap:8px;color:#fff;font-weight:600;font-size:17px}
  .contact .mark{width:16px;height:16px;background:var(--yellow);border-radius:3px}
  .c-mail{left:40px;top:1060px}
  .c-fb{left:360px;top:1090px}
  .c-ig{left:620px;top:1110px}
  .web-bar{position:absolute;left:70px;top:1140px;width:560px;height:70px;background:var(--bar);border-radius:0 36px 0 0;
    color:#fff;font-size:19px;font-weight:600;letter-spacing:10px;text-align:center;padding-top:16px}
</style>
</head>
<body>
<main class="flyer">
  <div class="photo-hero" role="img" aria-label="Photo of a young girl at a table looking at a fork of capsicum beside a bowl of fresh vegetables"></div>

  <div class="brand">
    <span class="brand-dot"></span>
    <span class="brand-name">Nourish Kin Network Australia</span>
  </div>

  <svg class="wave" viewBox="0 0 848 220" preserveAspectRatio="none" aria-hidden="true">
    <path d="M0 95 C180 40 330 60 470 110 C620 165 740 160 848 120 L848 220 L0 220Z" fill="#ffffff"/>
    <path d="M0 70 C200 20 340 50 480 100 C620 150 740 150 848 110 L848 135 C740 175 620 175 480 130 C340 80 200 60 0 105Z" fill="var(--green)"/>
    <path d="M0 80 C200 35 340 65 480 112 C620 160 740 160 848 122 L848 150 C740 190 620 190 470 145 C330 100 180 90 0 130Z" fill="var(--purple)"/>
    <path d="M0 130 C180 90 330 100 470 145 C620 190 740 190 848 150 L848 165 C740 205 620 205 470 160 C330 115 180 110 0 150Z" fill="var(--teal)"/>
  </svg>

  <section class="intro">
    <h1 class="headline">DOES YOUR CHILD<br>HAVE AN EATING DISORDER?</h1>
    <p class="subhead">Are you concerned your child has a problem with<br>eating, weight or body image?</p>
    <p class="lead">Parents and carers play a pivotal role in treatment &amp; recovery<br>of eating disorders</p>
    <p class="promise">NKNA will help you get the skills &amp; knowledge you need to<br>support your loved one through this illness</p>
  </section>

  <div class="grass"></div>

  <section class="board">
    <h2 class="board-title">Why NKNA exists</h2>
    <ul class="reasons">
      <li><svg class="tick" viewBox="0 0 14 14"><circle cx="7" cy="7" r="6" fill="none" stroke="#f5e11a" stroke-width="1.5"/><path d="M4 7.2l2 2 4-4.4" fill="none" stroke="#f5e11a" stroke-width="1.6"/></svg>NKNA supports families and carers of people with an eating disorder</li>
      <li><svg class="tick" viewBox="0 0 14 14"><circle cx="7" cy="7" r="6" fill="none" stroke="#f5e11a" stroke-width="1.5"/><path d="M4 7.2l2 2 4-4.4" fill="none" stroke="#f5e11a" stroke-width="1.6"/></svg>Early action is imperative</li>
      <li><svg class="tick" viewBox="0 0 14 14"><circle cx="7" cy="7" r="6" fill="none" stroke="#f5e11a" stroke-width="1.5"/><path d="M4 7.2l2 2 4-4.4" fill="none" stroke="#f5e11a" stroke-width="1.6"/></svg>NKNA will help guide you to appropriate resources &amp; support</li>
      <li><svg class="tick" viewBox="0 0 14 14"><circle cx="7" cy="7" r="6" fill="none" stroke="#f5e11a" stroke-width="1.5"/><path d="M4 7.2l2 2 4-4.4" fill="none" stroke="#f5e11a" stroke-width="1.6"/></svg>NKNA advocates for parents/carers to be actively involved in treatment team</li>
      <li><svg class="tick" viewBox="0 0 14 14"><circle cx="7" cy="7" r="6" fill="none" stroke="#f5e11a" stroke-width="1.5"/><path d="M4 7.2l2 2 4-4.4" fill="none" stroke="#f5e11a" stroke-width="1.6"/></svg>NKNA acknowledges the importance of well-being of ALL family members throughout the ED journey</li>
    </ul>
  </section>

  <div class="kid-left" role="img" aria-label="Cartoon illustration of a boy in an orange checked shirt waving beside the board"></div>
  <div class="kid-right" role="img" aria-label="Cartoon illustration of a girl in a red polka-dot dress waving beside the board"></div>

  <p class="partner">Uplift logo</p>
  <p class="pledge">Will endeavour to facilitate and advocate for families</p>

  <p class="contact c-mail"><svg width="18" height="13" viewBox="0 0 18 13"><rect x="0.5" y="0.5" width="17" height="12" fill="#f5e11a"/><path d="M1 1l8 6 8-6" fill="none" stroke="#2f5f12" stroke-width="1.3"/></svg>admin@nkna.org.au</p>
  <p class="contact c-fb"><span class="mark"></span>@nknaaustralia</p>
  <p class="contact c-ig"><span class="mark"></span>@nknaaustralia</p>

  <div class="web-bar">WWW.NKNA.ORG.AU</div>
</main>
</body>
</html>
```